The Ridgeway Aerial Group Flyer to entice people to call us.

We negotiate contracts for phone masts (commercial leases). We also sell phone masts, remove phone masts, oversee the build of phone masts etc but act only for landlords. Our website is www.ridgewayaerialgroup.co.uk and i would like the flyer to reflect the branding and colour scheme on it. Ideally, i would like a tri-fold flyer. One page should be our contact details. You can use the images i have uploaded but also, you can use some of your own if you feel there are appropriate (ie people etc). We want to project the image of looking after landlords who have phone masts and making them a lot of money. I can provide the section titles and wording.

Target Market(s)

Landowners, can be big corporations like Brambos or Utility companies- or farmers and people who own buildings.

Industry/Entity Type

Telecommunications

Font styles to use
Sans Serif

Requirements
Must have
• Must have our colour scheme from our website (www.ridgewayaerialgroup.co.uk), must look modern and catchy, must have our contact details, must have pictures of one stand alone mast (tower) and one rooftop mast. Must have our logo (which should be attached).
Nice to have
• Perhaps some pictures of people looking happy, maybe an old couple, maybe a picture of a corporate individual, punchy headings.

```html
<!DOCTYPE html>
<html lang="en">
<head>
<meta charset="utf-8">
<title>The Ridgeway Aerial Group – Flyer Panel</title>
<link href="https://fonts.googleapis.com/css2?family=Lato:wght@400;700&display=swap" rel="stylesheet">
<style>
  :root {
    --sky-top: #2f6fc4;
    --sky-bottom: #8db7e6;
    --field-green: #6e9a3c;
    --field-sky: #a9c8e8;
    --stripe-yellow: #f6c21b;
    --stripe-orange: #e8711d;
    --page-top: #eef3f8;
    --page-bottom: #f7f9fb;
    --ink: #2b2b2b;
    --heading: #1f1f1f;
    --strap-light: #8d8d8d;
    --strap-dark: #6f6f6f;
    --strap-text: #f4f4f4;
    --rule: #b9b9b9;
    --bullet: #3a3a3a;
  }
  * { box-sizing: border-box; margin: 0; padding: 0; }
  html, body { width: 849px; height: 1200px; overflow: hidden; }
  body {
    font-family: "Lato", sans-serif;
    color: var(--ink);
    background: var(--page-bottom);
  }
  .panel {
    position: relative;
    width: 849px;
    height: 1200px;
    background: linear-gradient(180deg, var(--page-top), var(--page-bottom));
    overflow: hidden;
  }
  .hero-photo {
    position: absolute; left: 0; top: 0; width: 849px; height: 203px;
    background: linear-gradient(180deg, var(--sky-top), var(--sky-bottom));
  }
  .footer-photo {
    position: absolute; left: 0; bottom: 0; width: 849px; height: 190px;
    background: linear-gradient(180deg, var(--field-sky) 0%, #cfdfe9 45%, var(--field-green) 80%, #557f2c 100%);
  }
  .stripe {
    position: absolute; left: 0; width: 849px; height: 8px;
    background: linear-gradient(90deg, var(--stripe-yellow) 0%, var(--stripe-yellow) 40%, var(--stripe-orange) 60%, var(--stripe-orange) 100%);
  }
  .stripe--top { top: 203px; }
  .stripe--bottom { top: 1002px; }
  .body-copy {
    position: absolute; top: 238px;
    font-size: 13.4px; line-height: 23px; text-align: justify;
  }
  .body-copy p + p { margin-top: 19px; }
  .body-copy--left { left: 49px; width: 300px; }
  .body-copy--right { left: 373px; width: 437px; }
  .services { position: absolute; left: 49px; top: 466px; }
  .services h2 {
    font-size: 16px; font-weight: 700; color: var(--heading); margin-bottom: 2px; line-height: 22px;
  }
  .services ul { list-style: none; }
  .services li {
    position: relative; padding-left: 22px; font-size: 15.3px; line-height: 23px;
  }
  .services li::before {
    content: ""; position: absolute; left: 3px; top: 8px;
    border-left: 4px solid transparent; border-right: 4px solid transparent;
    border-bottom: 7px solid var(--bullet);
  }
  .straplines { position: absolute; left: 373px; top: 466px; width: 476px; }
  .straplines h2 { font-size: 16.5px; font-weight: 700; color: var(--heading); line-height: 22px; margin-bottom: 8px; }
  .strap {
    padding: 7px 14px; font-size: 14.5px; line-height: 20px; color: var(--strap-text);
    background: var(--strap-light); margin-bottom: 8px;
  }
  .strap:nth-of-type(even) { background: var(--strap-dark); }
  .contact { position: absolute; left: 373px; top: 724px; width: 326px; font-size: 15.5px; line-height: 21px; }
  .contact h2 { font-size: 16px; font-weight: 700; color: var(--heading); line-height: 22px; }
  .contact address { font-style: normal; }
  .contact .rule { border: 0; border-top: 1px solid var(--rule); margin: 12px 0 10px; }
</style>
</head>
<body>
<main class="panel">
  <div class="hero-photo" role="img" aria-label="Photograph of a white phone mast tower against a blue sky"></div>
  <div class="stripe stripe--top"></div>

  <section class="body-copy body-copy--left">
    <p>Due to all the mergers, there have been and will be more sites which become duplicates in a network and surplus to requirements. Landlords with mobile phone masts that are no longer required are receiving letters stating that the operator wishes to serve the break clause and vacate the site. In some instances, The Ridgeway Aerial Group can stop this happening. If not, we can often negotiate a substantial settlement.</p>
  </section>

  <section class="body-copy body-copy--right">
    <p>Phone masts which the operators wish to retain are being subjected to rent reductions. Should the reduction be refused, the operator may threaten to leave the site. All threats should be taken seriously and professional advice should be sought. There is often opportunity for negotiation. We can in most cases, prevent the rent reduction all together or significantly reduce it via our Rent Protection service.</p>
    <p>Landlords should not sign anything until they have sought professional advice</p>
  </section>

  <section class="services">
    <h2>Our Services</h2>
    <ul>
      <li>Rent Reviews</li>
      <li>Lease Renewals</li>
      <li>Network Consolidation Issues</li>
      <li>Site Shares</li>
      <li>Rent Protection</li>
      <li>Equipment Upgrades</li>
      <li>Mast Removals / Decommissioning</li>
      <li>Mast Sales and Marketing</li>
      <li>Land Marketing for Masts</li>
      <li>Mast Management and Portfolios</li>
      <li>Safety Testing</li>
    </ul>
  </section>

  <section class="straplines">
    <h2>Strap lines that can be inserted throughout the leaflet:</h2>
    <p class="strap">“Call us and we can take the hassle away”</p>
    <p class="strap">“We can help you swap your rent for a large cash lump sum”</p>
    <p class="strap">“If you would like to know what rent your mast should be achieving, check out the free rent estimation service on our website”</p>
    <p class="strap">“Make the most from your phone mast”</p>
  </section>

  <section class="contact">
    <h2>Contact Us</h2>
    <address>
      The Ridgeway Aerial Group Ltd<br>
      The Beacon Offices,<br>
      Kestrel Business Park,<br>
      Hill Farm,<br>
      Shropshire,<br>
      SY99 2QZ
    </address>
    <hr class="rule">
    <p>t: 01632 960543<br>
      f: 01632 960222<br>
      e: info@ridgewayaerialgroup.co.uk<br>
      w: www.ridgewayaerialgroup.co.uk</p>
  </section>

  <div class="stripe stripe--bottom"></div>
  <div class="footer-photo" role="img" aria-label="Photograph of a lattice phone mast with equipment cabins in a green field"></div>
</main>
</body>
</html>
```